Restaurant needs a vertical banner for fried catfish

Our restaurant is looking for an eye-catching 78.75in. x 36in. vertical physical banner ad for our fried catfish. Photos for the fried catfish will be provided as a reference but we will also accept anything similar to the photo. We will be using the following as our receptacle: https://www.plankoria.example/banner-stand/retractable-banner-stands/
The design must incorporate the following flavor texts:
Fried Catfish
Always Fresh!
Made from Scratch
Hand-cut Fillets
The Best Catfish in Texas
Served with fries, hush puppies, and a 32oz fountain drink
Also available by the pound!
The final design should be creative, professional, and eye-catching for customers.
Updates
Colors
Designer to choose colors to be used in the design.
Requirements
Must have
- We are open to any and all design elements, albeit the 'flavor texts' should not overpower, but complement the fried catfish photo. 'Fried Catfish' can be used in lieu of a main title/logo.
Nice to have
- Transparent or textured backgrounds that can encompass any or all part of the banner such as a cutting board, shadows, abstract, etc to show depth are a plus.
- Use of vectors or objects such as ribbons or shapes to encapsulate the 'flavor texts' are also encouraged.

```html
<!DOCTYPE html>
<html lang="en">
<head>
<meta charset="utf-8">
<title>Fried Catfish Banner</title>
<link rel="stylesheet" href="https://fonts.googleapis.com/css2?family=Asap+Condensed:wght@600;700&family=Fira+Sans+Extra+Condensed:wght@800;900&family=Permanent+Marker&display=swap">
<style>
  :root {
    --page-bg: #eebf7f;
    --yellow: #fdd20a;
    --black: #0a0a0a;
    --white: #ffffff;
    --pattern: #f1f1f1;
    --food-dark: #5a1e0c;
    --food-mid: #c7781f;
    --food-light: #e9a640;
  }
  * { margin: 0; padding: 0; box-sizing: border-box; }
  html, body { width: 1200px; height: 1026px; overflow: hidden; background: var(--page-bg); }
  .canvas { position: relative; width: 1200px; height: 1026px; }
  .banner {
    position: absolute; left: 400px; top: 24px;
    width: 453px; height: 1107px;
    transform: scale(0.885); transform-origin: 0 0;
    background: var(--pattern);
    overflow: hidden;
    box-shadow: 0 6px 24px rgba(0,0,0,.25);
  }
  .banner > * { position: absolute; }
  .food-photo { left: 0; top: 0; width: 453px; height: 430px;
    background: radial-gradient(ellipse at 60% 65%, var(--food-light) 0%, var(--food-mid) 35%, var(--food-dark) 80%);
    border-bottom-left-radius: 60% 18%; border-bottom-right-radius: 40% 14%; }
  .burst { left: 0; top: 0; width: 270px; height: 220px; }
  .burst-text { left: 28px; top: 18px; font-family: "Asap Condensed", sans-serif; font-weight: 700;
    font-size: 64px; line-height: 76px; color: var(--black); transform: skewX(-4deg); }
  .title-band { left: 0; top: 450px; width: 453px; height: 270px; }
  .catfish-art { left: 30px; top: 475px; width: 190px; height: 125px;
    background: radial-gradient(ellipse, #3a3a3a 0%, #111 70%); border-radius: 50% 40% 45% 55%; }
  .title { font-family: "Permanent Marker", cursive; color: var(--white);
    -webkit-text-stroke: 3px var(--black); paint-order: stroke fill; text-shadow: 3px 3px 0 var(--black); }
  .title-fried { left: 238px; top: 478px; font-size: 72px; transform: rotate(-8deg); }
  .title-catfish { left: 20px; top: 568px; font-size: 104px; transform: rotate(-8deg); letter-spacing: -2px; }
  .features { left: 0; top: 735px; width: 453px; height: 175px; background: var(--black);
    border-top: 3px solid var(--yellow); border-bottom: 3px solid var(--yellow); padding: 14px 20px 0 26px;
    list-style: none; font-family: "Asap Condensed", sans-serif; font-weight: 600; font-size: 28px;
    line-height: 34px; color: var(--yellow); }
  .features li { position: relative; padding-left: 24px; margin-bottom: 8px; }
  .features li::before { content: ""; position: absolute; left: 0; top: 13px; width: 11px; height: 11px;
    border-radius: 3px; background: var(--yellow); }
  .tagline { left: 34px; top: 925px; font-family: "Fira Sans Extra Condensed", sans-serif; font-weight: 900;
    color: var(--yellow); -webkit-text-stroke: 3px var(--black); paint-order: stroke fill; white-space: nowrap; }
  .tagline small { font-size: 27px; font-weight: 800; }
  .tagline strong { font-size: 86px; line-height: 1; }
  .pound-pill { left: 28px; top: 1032px; width: 392px; height: 40px; border-radius: 20px; background: var(--black);
    color: var(--yellow); font-family: "Asap Condensed", sans-serif; font-weight: 700; font-size: 26px;
    letter-spacing: 1.5px; text-align: center; line-height: 40px; }
</style>
</head>
<body>
<div class="canvas">
  <div class="banner">
    <div class="food-photo" role="img" aria-label="Photo of fried catfish fillets on a plate with fries, lemon wedge, lettuce and ketchup"></div>
    <svg class="burst" viewBox="0 0 270 220" aria-hidden="true">
      <polygon points="0,0 245,0 235,22 262,40 238,62 258,85 230,100 248,125 218,132 228,160 196,160 200,190 170,180 162,210 138,190 122,215 108,188 88,210 76,182 52,200 44,170 18,185 16,158 0,160"
        fill="var(--yellow)" stroke="var(--black)" stroke-width="4"/>
    </svg>
    <div class="burst-text">Always<br>Fresh!</div>
    <svg class="title-band" viewBox="0 0 453 270" aria-hidden="true">
      <polygon points="0,18 453,5 453,258 0,265" fill="var(--yellow)" stroke="var(--black)" stroke-width="4"/>
    </svg>
    <div class="catfish-art" role="img" aria-label="Black and white catfish illustration"></div>
    <div class="title title-fried">Fried</div>
    <div class="title title-catfish">Catfish</div>
    <ul class="features">
      <li>Made from Scratch</li>
      <li>Hand-cut Fillets</li>
      <li>Served with fries, hush puppies, &amp; a 32oz fountain drink</li>
    </ul>
    <div class="tagline"><small>The Best Catfish in </small><strong>Texas</strong></div>
    <div class="pound-pill">Also available by the pound!</div>
  </div>
</div>
</body>
</html>
```